Electrician Letterhead Design RMV

We need some letterhead for our bills and other papers.
Customer address is on the right side (Swiss format)
A4 format

Design should also be applicable on Cards

Target Market(s)

Private Customers, Small Business

Industry/Entity Type

Electrician

Other font styles liked:
• incised 901

Colors
00AB8E
00BBA5
67D7C9
C6EFE9
E9F9F6

```html
<!DOCTYPE html>
<html lang="de">
<head>
<meta charset="utf-8">
<title>RMV Letterhead</title>
<link href="https://fonts.googleapis.com/css2?family=Open+Sans:wght@400;800&family=Orbitron:wght@600&display=swap" rel="stylesheet">
<style>
  :root {
    --teal-deep: #00AB8E;
    --teal: #00BBA5;
    --teal-light: #67D7C9;
    --mint: #C6EFE9;
    --mint-pale: #E9F9F6;
    --ink: #3a3a3a;
    --paper: #ffffff;
    --backdrop: #dcdcdc;
  }
  * { box-sizing: border-box; margin: 0; padding: 0; }
  html, body {
    width: 1200px;
    height: 1163px;
    overflow: hidden;
    background: var(--backdrop);
  }
  .sheet {
    position: absolute;
    left: 211px;
    top: 31px;
    width: 778px;
    height: 1100px;
    background: var(--paper);
    box-shadow: 0 6px 24px rgba(0,0,0,0.12);
  }
  .sheet__edge {
    position: absolute;
    top: 0;
    right: 0;
    width: 9px;
    height: 100%;
    background: var(--teal-deep);
  }
  .letterhead {
    position: absolute;
    left: 62px;
    top: 64px;
    color: var(--ink);
  }
  .brand {
    display: flex;
    align-items: center;
    gap: 10px;
  }
  .brand__name {
    font-family: "Open Sans", sans-serif;
    font-weight: 800;
    font-size: 58px;
    line-height: 1;
    letter-spacing: 1px;
    color: var(--teal-deep);
  }
  .brand__square {
    width: 16px;
    height: 16px;
    background: var(--teal-deep);
  }
  .company {
    margin-top: 8px;
    font-family: "Orbitron", sans-serif;
    font-weight: 600;
    font-size: 12px;
    letter-spacing: 0.3px;
    color: #222;
  }
  .address {
    margin-top: 10px;
    font-family: "Open Sans", sans-serif;
    font-size: 12.5px;
    line-height: 1.35;
  }
  .contact {
    margin-top: 8px;
    list-style: none;
    font-family: "Open Sans", sans-serif;
    font-size: 12.5px;
    line-height: 1.35;
  }
  .contact__item {
    display: flex;
    align-items: center;
    gap: 7px;
  }
  .contact__icon {
    width: 12px;
    height: 12px;
    flex: none;
  }
</style>
</head>
<body>
  <main class="sheet">
    <header class="letterhead">
      <div class="brand">
        <span class="brand__name">RMV</span>
        <span class="brand__square"></span>
      </div>
      <p class="company">Elektrotechnik Rinaldi GmbH</p>
      <address class="address">
        Suite 102 Street name,<br>
        State, Zip 2034, Country
      </address>
      <ul class="contact">
        <li class="contact__item">
          <svg class="contact__icon" viewBox="0 0 12 12" aria-hidden="true"><circle cx="6" cy="6" r="6" fill="var(--teal-deep)"/><path d="M4 3.2l1 1.3-.6.7a4 4 0 0 0 2.4 2.4l.7-.6 1.3 1-.6 1A5 5 0 0 1 3 4z" fill="#fff"/></svg>
          <span>+41-5550-123480</span>
        </li>
        <li class="contact__item">
          <svg class="contact__icon" viewBox="0 0 12 12" aria-hidden="true"><circle cx="6" cy="6" r="6" fill="var(--teal-deep)"/><rect x="4" y="2.6" width="4" height="6.8" rx="0.8" fill="#fff"/></svg>
          <span>+41-5550-1234817</span>
        </li>
        <li class="contact__item">
          <svg class="contact__icon" viewBox="0 0 12 12" aria-hidden="true"><circle cx="6" cy="6" r="6" fill="var(--teal-deep)"/><rect x="3" y="4" width="6" height="4.2" fill="#fff"/><path d="M3 4l3 2.2L9 4" stroke="var(--teal-deep)" stroke-width="0.7" fill="none"/></svg>
          <span>info@rinaldielektro.ch</span>
        </li>
        <li class="contact__item">
          <svg class="contact__icon" viewBox="0 0 12 12" aria-hidden="true"><circle cx="6" cy="6" r="6" fill="var(--teal-deep)"/><circle cx="6" cy="6" r="3.2" fill="none" stroke="#fff" stroke-width="0.8"/><path d="M2.8 6h6.4M6 2.8v6.4" stroke="#fff" stroke-width="0.6"/></svg>
          <span>www.rinaldielektro.ch</span>
        </li>
      </ul>
    </header>
    <div class="sheet__edge"></div>
  </main>
</body>
</html>
```